Letterhead design for Dental Practice - Ashby Lane Dental Care

Letterhead for Private Dental Practice. To be used for all official correspondance and for printing treatment details on to be given to patients.

Target Market(s)

Private dental patients

Industry/Entity Type

Dental Clinic

Font styles to use
Other font styles liked:
• nexa-light

Colors
33a6d7
1c66ac
85abd2

Requirements
Must have
• info in the footer and header needs to be 3.5cm from upper/lower boader of paper, see photo in uploaded files
• info details:
• tel. 0115 947 3051
• email info@ashbylanedc.co.uk
• ashbylanedentalcare.co.uk
• 17b Ashby Lane West Bridgford Nottingham NG2 7QT
• nexa-light font as in uploaded logo files
Should not have
• No funny tooth pictures

```html
<!DOCTYPE html>
<html lang="en">
<head>
<meta charset="utf-8">
<title>Ashby Lane Dental Care – Letterhead</title>
<link rel="stylesheet" href="https://fonts.googleapis.com/css2?family=Open+Sans:wght@400;600&family=Quicksand:wght@400&display=swap">
<style>
  :root {
    --brand-blue: #33a6d7;
    --corner-blue: #159fdc;
    --corner-grey: #535456;
    --ink: #3a3a3a;
    --ink-soft: #444;
    --paper: #ffffff;
    --signature-tone: #e6e8ea;
  }
  * { margin: 0; padding: 0; box-sizing: border-box; }
  html, body { width: 1040px; height: 1200px; overflow: hidden; background: var(--paper); }
  .letterhead {
    position: relative;
    width: 1040px;
    height: 1200px;
    background: var(--paper);
    font-family: "Open Sans", sans-serif;
    color: var(--ink);
    overflow: hidden;
  }
  .corner { position: absolute; display: block; }
  .corner--top { left: 0; top: 0; }
  .corner--bottom { right: 0; bottom: 0; }

  .practice-name {
    position: absolute;
    left: 99px;
    top: 138px;
    font-family: "Open Sans", sans-serif;
    font-weight: 400;
    font-size: 22px;
    line-height: 28px;
    color: var(--ink);
  }

  .contact {
    position: absolute;
    right: 108px;
    top: 72px;
    list-style: none;
    text-align: right;
    font-family: "Quicksand", sans-serif;
    font-size: 15px;
    line-height: 19px;
    color: var(--ink);
  }
  .contact li { display: flex; justify-content: flex-end; align-items: center; gap: 6px; }
  .contact svg { width: 11px; height: 11px; flex: none; }

  .letter-body {
    position: absolute;
    left: 99px;
    top: 216px;
    width: 840px;
    font-size: 16px;
    color: var(--ink-soft);
  }
  .issue-date { line-height: 20px; }
  .recipient { margin-top: 16px; line-height: 19px; }
  .salutation { margin-top: 47px; line-height: 20px; }
  .paragraph {
    margin-top: 34px;
    line-height: 27px;
    text-align: justify;
    hyphens: auto;
  }
  .paragraph + .paragraph { margin-top: 27px; }
  .sign-off { margin-top: 54px; line-height: 20px; }
  .signature {
    margin-top: 14px;
    width: 240px;
    height: 30px;
    border-radius: 4px;
    background: linear-gradient(90deg, var(--signature-tone), #f3f4f5);
  }
  .signatory { margin-top: 12px; font-size: 19px; font-weight: 600; line-height: 24px; color: #333; }
  .role { margin-top: 4px; line-height: 20px; }

  .address {
    position: absolute;
    left: 99px;
    top: 1119px;
    font-family: "Quicksand", sans-serif;
    font-style: normal;
    font-size: 15px;
    line-height: 19px;
    color: var(--ink);
  }
</style>
</head>
<body>
<main class="letterhead">
  <svg class="corner corner--top" width="280" height="245" viewBox="0 0 280 245" aria-hidden="true">
    <path d="M0 0 H272 C160 20 40 80 0 240 Z" fill="var(--corner-grey)"/>
  </svg>
  <svg class="corner corner--bottom" width="260" height="220" viewBox="0 0 260 220" aria-hidden="true">
    <path d="M260 0 V220 H0 C80 200 150 175 180 150 C220 115 240 60 260 0 Z" fill="var(--corner-blue)"/>
  </svg>

  <p class="practice-name">Ashby Lane Dental Care</p>

  <ul class="contact">
    <li>0115 947 3051
      <svg viewBox="0 0 12 12" aria-hidden="true"><path d="M1 4 C1 2 3 1.5 6 1.5 S11 2 11 4 L9 5 L8 3.5 H4 L3 5 Z M3 6 H9 L10 10.5 H2 Z" fill="var(--brand-blue)"/></svg>
    </li>
    <li>info@ashbylanedc.co.uk
      <svg viewBox="0 0 12 12" aria-hidden="true"><rect x="1" y="2.5" width="10" height="7" rx="1" fill="var(--brand-blue)"/><path d="M1.5 3 L6 6.5 L10.5 3" stroke="#fff" stroke-width="1" fill="none"/></svg>
    </li>
    <li>www.ashbylanedentalcare.co.uk
      <svg viewBox="0 0 12 12" aria-hidden="true"><circle cx="6" cy="6" r="5" fill="var(--brand-blue)"/><path d="M1 6 H11 M6 1 C3.5 4 3.5 8 6 11 M6 1 C8.5 4 8.5 8 6 11" stroke="#fff" stroke-width="0.8" fill="none"/></svg>
    </li>
  </ul>

  <section class="letter-body">
    <p class="issue-date">Issuing Date: May 5, 2018</p>
    <p class="recipient">Name Of Employee Mr. XYZABC<br>Address of Employee<br>Address Line 2 etc..</p>
    <p class="salutation">Dear Mr.XYZABC</p>
    <p class="paragraph">Lorem Ipsum has been the industry's standard dummy text ever since the 1500s, when an unknown printer took a galley of type and scrambled it to make a type specimen book. It has survived not only five centuries, but also the leap into electronic typesetting, remaining essentially unchanged. It was popularised in the 1960s with the release of Typeline sheets containing Lorem Ipsum passages, and more recently with desktop publishing software like Folio Layout including versions of Lorem Ipsum.</p>
    <p class="paragraph">Lorem Ipsum is simply dummy text of the printing and typesetting industry. Lorem Ipsum has been the industry's standard dummy text ever since the 1500s, when an unknown printer took a galley of type and scrambled it to make a type specimen book.</p>
    <p class="paragraph">It has survived not only five centuries, but also the leap into electronic typesetting, remaining essentially unchanged. It was popularised in the 1960s with the release of Typeline sheets containing Lorem IpsumIpsum passages.</p>
    <p class="sign-off">Yours Sincerely</p>
    <div class="signature" role="img" aria-label="Handwritten signature of Daniel Hartley"></div>
    <p class="signatory">Daniel Hartley</p>
    <p class="role">Managing Director</p>
  </section>

  <address class="address">17b Ashby Lane West<br>Bridgford Nottingham NG2 7QT</address>
</main>
</body>
</html>
```